Create a website in Wordpress for an interior design company

Create a website for our interior design company 'Roomora'

-Color preferences - Neutral and warm colors. Nothing too bright
-Aesthetic: Modern, Minimalist, Classic, Mature, Luxury
-Mission Statement: Transforming homes into personalized dream spaces through exceptional interior design, meticulous attention to detail, and a touch of the unexpected.
-Brand Values: innovation, creativity, passion and sustainability

Examples: https://www.lenamarchwoodinteriors.com.au/
https://www.tidecraftstudio.com/

About
Portfolio
Inquire page

```html
<!DOCTYPE html>
<html lang="en">
<head>
<meta charset="utf-8">
<title>Roomora Interior Design</title>
<link href="https://fonts.googleapis.com/css2?family=Playfair+Display:wght@500;600;700&family=Poppins:wght@300;400;500&family=Teko:wght@400;500&display=swap" rel="stylesheet">
<style>
:root{
  --tan:#b4956d;
  --tan-soft:#c7ad8c;
  --ink:#1f1f1f;
  --text:#7a7a7a;
  --muted:#9a9a9a;
  --cream:#f7f3f1;
  --dark:#1b1b1b;
  --footer:#2b2a3a;
  --white:#ffffff;
  --line:#e4e0dc;
}
*{margin:0;padding:0;box-sizing:border-box}
html,body{width:1200px;height:4345px;overflow:hidden}
body{font-family:"Poppins",sans-serif;color:var(--ink);background:var(--white);position:relative}
.abs{position:absolute}
.serif{font-family:"Playfair Display",serif}
.cond{font-family:"Teko",sans-serif}
section,header,footer{position:absolute;left:0;width:1200px}
.eyebrow{font-size:10px;letter-spacing:3px;color:var(--tan);text-transform:uppercase}
.center{text-align:center;left:0;width:1200px}
.btn{background:var(--tan);color:#fff;font-size:12px;letter-spacing:1px;display:flex;align-items:center;justify-content:center}

/* header */
.site-header{top:0;height:74px;background:#fff}
.brand{display:flex;align-items:center;gap:8px;font-family:"Playfair Display",serif;font-size:18px;color:var(--tan);font-weight:500}
.brand .dot{width:10px;height:10px;background:var(--tan)}
.nav a{position:absolute;top:27px;font-size:13px;color:var(--ink);text-decoration:none}

/* hero */
.hero{top:74px;height:555px;background:radial-gradient(ellipse at 70% 70%,#6b5534 0%,transparent 45%),linear-gradient(180deg,#1c2440 0%,#232a44 40%,#2b2a2a 75%,#151515 100%)}
.hero h1{font-family:"Playfair Display",serif;color:#fff;font-weight:700;font-size:60px;line-height:74px}
.hero p{color:#f1ece6;font-size:13px;line-height:25px}
.socials{display:flex;gap:20px}
.socials span{width:12px;height:12px;border:1.5px solid #fff;border-radius:50%}

/* about */
.about{top:629px;height:551px;background:#fff}
.about h2{font-family:"Playfair Display",serif;font-size:31px;font-weight:600;line-height:45px}
.about p{font-size:12.5px;line-height:25px;color:var(--text)}
.tags{display:flex;font-size:8px;letter-spacing:1.5px;color:var(--muted)}
.tags span{padding:0 10px;border-left:1px solid var(--line)}
.tags span:first-child{padding-left:0;border:0}

/* services */
.services{top:1180px;height:645px;background:var(--cream)}
.section-title{font-family:"Playfair Display",serif;font-size:31px;font-weight:500}
.cards{left:158px;top:225px;width:903px;height:323px;display:flex;background:#fff}
.card{flex:1;padding:55px 31px 0;border-left:1px solid #f0ebe7}
.card:first-child{border:0}
.num{font-family:"Teko",sans-serif;font-size:46px;line-height:40px;color:transparent;-webkit-text-stroke:1px var(--tan)}
.card h3{margin-top:25px;font-size:13px;letter-spacing:1px;color:var(--tan);font-weight:500}
.card p{margin-top:15px;font-size:11.5px;line-height:24px;color:var(--text)}
.card .more{display:block;margin-top:22px;font-family:"Teko",sans-serif;font-size:15px;color:var(--ink)}

/* portfolio */
.portfolio{top:1825px;height:989px;background:var(--dark)}
.filters{left:683px;top:73px;width:348px;height:47px;border-radius:24px;background:#222;display:flex;align-items:center;justify-content:center;gap:16px;font-size:9px;letter-spacing:1px;color:#a89a8a}
.filters i{width:5px;height:5px;border-radius:50%;background:#5ec9b5;display:block}
.filters .active{color:#5ec9b5}
.work-img{position:absolute}
.work-cap{position:absolute;text-align:center;width:357px}
.work-cap b{display:block;font-family:"Teko",sans-serif;font-weight:500;font-size:15px;letter-spacing:3px;color:var(--tan)}
.work-cap small{display:block;margin-top:6px;font-family:"Teko",sans-serif;font-size:11px;letter-spacing:2px;color:#8c7a62}

/* stats */
.stats{top:2814px;height:246px;background:#fff}
.stat{position:absolute;text-align:center;width:200px}
.stat b{display:block;font-family:"Teko",sans-serif;font-size:48px;font-weight:400;color:var(--tan);line-height:44px}
.stat small{display:block;margin-top:4px;font-size:9px;letter-spacing:2px;color:var(--muted)}

/* contact */
.contact{top:3060px;height:485px;background:var(--cream)}
.info-card{position:absolute;top:225px;width:278px;height:187px;background:#fff;text-align:center}
.info-card svg{margin-top:28px}
.info-card h4{margin-top:12px;font-family:"Teko",sans-serif;font-size:16px;letter-spacing:2px;color:var(--tan);font-weight:500}
.info-card p{margin-top:10px;font-family:"Teko",sans-serif;font-size:14px;letter-spacing:1px;line-height:22px;color:var(--muted)}

/* map + form */
.reach{top:3545px;height:472px;background:#fff}
.map{left:0;top:0;width:608px;height:472px;background:linear-gradient(135deg,#e9e9e7,#dcdcd8 55%,#e5e5e2)}
.form h3{font-family:"Playfair Display",serif;font-size:24px;font-weight:600}
.form label{position:absolute;font-size:13px;font-weight:500}
.form .field{position:absolute;left:0;width:477px;border:1px solid #cfcfcf;font-size:12px;color:#aaa;padding:5px 4px}

/* footer */
.site-footer{top:4017px;height:328px;background:var(--footer);color:#a9a8b8}
.site-footer .brand{color:#fff}
.site-footer .brand .dot{background:#fff}
.foot-head{font-size:9px;letter-spacing:2px;color:#8d8ca0}
.foot-list{font-size:11px;line-height:33px;color:#d8d7e4}
.foot-list li{list-style:none}
.foot-list li::before{content:"›";margin-right:8px}
.fsocial{display:flex;gap:14px}
.fsocial span{width:22px;height:22px;border-radius:50%;background:#fff}
</style>
</head>
<body>

<header class="site-header">
  <div class="abs brand" style="left:165px;top:25px"><span class="dot"></span>Roomora</div>
  <nav class="nav">
    <a style="left:357px">Home</a>
    <a style="left:448px">About</a>
    <a style="left:540px">Services</a>
    <a style="left:647px">Projects</a>
    <a style="left:751px">Contact</a>
  </nav>
  <div class="abs btn" style="left:887px;top:17px;width:148px;height:37px;font-size:11px">GET IN TOUCH</div>
</header>

<section class="hero" role="img" aria-label="Modern house with lit interior at dusk, wooden deck and trees">
  <h1 class="abs center" style="top:128px">Roomora<br>Interior Design</h1>
  <p class="abs center" style="top:296px">Transforming homes into personalized dream spaces through exceptional<br>interior design, meticulous attention to detail, and a touch of the unexpected.</p>
  <div class="abs btn" style="left:527px;top:358px;width:149px;height:38px">Discover Work</div>
  <div class="abs socials" style="left:20px;top:522px" aria-label="Social links"><span></span><span></span><span></span><span></span></div>
</section>

<section class="about">
  <div class="abs eyebrow" style="left:189px;top:102px">About Us</div>
  <h2 class="abs" style="left:189px;top:128px">Best Designers<br>Architectures For You.</h2>
  <p class="abs" style="left:189px;top:232px;width:420px">Architecture bibendum pharetra eleifend. Suspendisse vel volutpat purus, sit amet bibendum nisl. Cras mollis turpis a ipsum ultes, nec condimentum ipsum consequat. Mauris vitae consequat nibh, vitae interdum mi.</p>
  <div class="abs tags" style="left:189px;top:352px"><span>ARCHITECTURE</span><span>INTERIOR DESIGN</span><span>FURNITURE</span></div>
  <div class="abs btn" style="left:189px;top:395px;width:127px;height:36px">Read More</div>
  <div class="abs" role="img" aria-label="Minimal dining room with white chairs, wood table and window" style="left:617px;top:122px;width:435px;height:290px;background:linear-gradient(180deg,#d9d5cf 0%,#c9c3ba 55%,#b59c7b 100%)"></div>
</section>

<section class="services">
  <div class="abs eyebrow center" style="top:95px">Best Features</div>
  <h2 class="abs section-title center" style="top:117px">Our Services</h2>
  <div class="abs cards">
    <div class="card"><div class="num">01</div><h3>ARCHITECTURE</h3><p>Cras mollis turpis a ipsum ultes, nec cond imentum ipsum consequat.</p><span class="more">Read More</span></div>
    <div class="card"><div class="num">02</div><h3>INTERIOR DESIGN</h3><p>Cras mollis turpis a ipsum ultes, nec cond imentum ipsum consequat.</p><span class="more">Read More</span></div>
    <div class="card"><div class="num">03</div><h3>3D MODELING</h3><p>Cras mollis turpis a ipsum ultes, nec cond imentum ipsum consequat.</p><span class="more">Read More</span></div>
    <div class="card"><div class="num">04</div><h3>FURNITURE DESIGN</h3><p>Cras mollis turpis a ipsum ultes, nec cond imentum ipsum consequat.</p><span class="more">Read More</span></div>
  </div>
</section>

<section class="portfolio">
  <div class="abs filters"><span class="active">ALL</span><i></i><span>RESIDENTIAL</span><i></i><span>COMMERCIAL</span><i></i><span>OFFICE</span></div>

  <div class="work-img" role="img" aria-label="Living room with black leather sofa and large gabled window" style="left:212px;top:161px;width:357px;height:200px;background:linear-gradient(180deg,#bcbcb8,#8e8e8a 70%,#3a3a3a)"></div>
  <div class="work-cap" style="left:212px;top:382px"><b>MODERN TOWNHOUSE</b><small>ARCHITECTURE . MODERN</small></div>

  <div class="work-img" role="img" aria-label="Dining room with white chairs and wood table" style="left:648px;top:161px;width:357px;height:237px;background:linear-gradient(180deg,#d6d2cc,#c5bfb6 55%,#b39a78)"></div>
  <div class="work-cap" style="left:648px;top:420px"><b>MODERN TOWNHOUSE</b><small>ARCHITECTURE . MODERN</small></div>

  <div class="work-img" role="img" aria-label="Dark kitchen with wood counter and bar stools" style="left:212px;top:507px;width:357px;height:238px;background:linear-gradient(180deg,#3b3b3b,#555 50%,#b88d4e 75%,#e8e4de)"></div>
  <div class="work-cap" style="left:212px;top:765px"><b>MODERN TOWNHOUSE</b><small>ARCHITECTURE . MODERN</small></div>

  <div class="work-img" role="img" aria-label="Study corner with desk, armchair, plant and arched window" style="left:648px;top:545px;width:357px;height:258px;background:linear-gradient(180deg,#e2e0dc,#cfcbc4 60%,#9c8466)"></div>
  <div class="work-cap" style="left:648px;top:825px"><b>MODERN TOWNHOUSE</b><small>ARCHITECTURE . MODERN</small></div>
</section>

<section class="stats">
  <div class="stat" style="left:52px;top:88px"><b>352</b><small>PROJECTS COMPLETED</small></div>
  <div class="stat" style="left:356px;top:88px"><b>567</b><small>SATISFIED CLIENTS</small></div>
  <div class="stat" style="left:660px;top:88px"><b>656</b><small>MONTHLY REVENUE</small></div>
  <div class="stat" style="left:966px;top:88px"><b>17</b><small>AWARDS WON</small></div>
</section>

<section class="contact">
  <div class="abs eyebrow center" style="top:96px">Keep In Touch</div>
  <h2 class="abs section-title center" style="top:118px">Contact Us</h2>
  <div class="info-card" style="left:169px">
    <svg width="20" height="24" viewBox="0 0 20 24" fill="none" stroke="#8a8a8a" stroke-width="1.5"><rect x="4" y="2" width="12" height="20" rx="2"/><line x1="9" y1="18" x2="11" y2="18"/></svg>
    <h4>CALL US</h4><p>+1 (555) 0142 7788<br>+1 (555) 0198 3346</p>
  </div>
  <div class="info-card" style="left:469px">
    <svg width="24" height="24" viewBox="0 0 24 24" fill="none" stroke="#8a8a8a" stroke-width="1.5"><path d="M3 10 12 3l9 7v10H3z"/><path d="M3 10l9 6 9-6"/></svg>
    <h4>EMAIL US</h4><p>contact@roomorastudio.com<br>hello@roomorastudio.com</p>
  </div>
  <div class="info-card" style="left:770px">
    <svg width="24" height="24" viewBox="0 0 24 24" fill="none" stroke="#8a8a8a" stroke-width="1.5"><path d="M3 6l6-2 6 2 6-2v14l-6 2-6-2-6 2z"/><line x1="9" y1="4" x2="9" y2="18"/><line x1="15" y1="6" x2="15" y2="20"/></svg>
    <h4>ADDRESS</h4><p>42 Alder Lane, Marlow Vale, Greater<br>Marlow MV4 2QT, United Kingdom</p>
  </div>
</section>

<section class="reach">
  <div class="abs map" role="img" aria-label="Street map of the studio's surrounding area"></div>
  <div class="abs form" style="left:723px;top:0;width:477px;height:472px">
    <h3 class="abs" style="left:0;top:78px">Contact Info.</h3>
    <label style="top:117px">Name</label>
    <div class="field" style="top:138px;height:30px">Name</div>
    <label style="top:180px">Email</label>
    <div class="field" style="top:201px;height:30px">Email</div>
    <label style="top:244px">Message</label>
    <div class="field" style="top:265px;height:57px">Message</div>
    <div class="abs btn" style="left:0;top:339px;width:477px;height:37px;font-size:12px">Send</div>
  </div>
</section>

<footer class="site-footer">
  <div class="abs brand" style="left:157px;top:70px"><span class="dot"></span>Roomora</div>
  <p class="abs" style="left:157px;top:115px;width:210px;font-size:10.5px;line-height:17px">Transforming homes into personalized dream spaces.</p>
  <div class="abs fsocial" style="left:160px;top:176px" aria-label="Social links"><span></span><span></span><span></span><span></span></div>

  <div class="abs foot-head" style="left:424px;top:62px">USEFUL LINKS</div>
  <ul class="abs foot-list" style="left:424px;top:86px"><li>Interior Design</li><li>About Us</li><li>Our Portfolio</li><li>Contact Us</li></ul>

  <div class="abs foot-head" style="left:645px;top:62px">CONTACT US</div>
  <div class="abs" style="left:645px;top:92px;font-size:10.5px;line-height:34px">☐ +1 (555) 0142 7788<br>☏ +1 (555) 0198 3346<br>contact@roomorastudio.com<br>hello@roomorastudio.com</div>

  <div class="abs foot-head" style="left:871px;top:62px">VISIT</div>
  <div class="abs" style="left:871px;top:92px;font-size:10.5px;line-height:32px">42 Alder Lane,<br>Marlow Vale, Greater Marlow<br>MV4 2QT, United Kingdom</div>

  <div class="abs" style="left:157px;top:298px;font-size:10px">© 2022,Roomora Made with passion by <b style="color:#d8d7e4">Fernlight Studio.</b></div>
  <div class="abs" style="left:915px;top:298px;font-size:10px;word-spacing:6px">Home | Policy | FAQ</div>
</footer>

</body>
</html>
```